WordPress Site That Reviews Footwear

We need a wordpress web design for an affiliate site called TarnWisp. We review and do roundups on footwear products. The final design should be clean and mobile friendly. The site should be built with Gutenberg page builder. We like the design of https://petalharvin.com/.

Target Market(s)

USA

Industry/Entity Type

Footwear

Logo Text

TarnWisp

Number of Pages Required

4 page

Font styles to use
Serif
Sans Serif

Requirements
Must have
• Wordpress site
Blog post
Page
Categories
Homepage

```html
<!DOCTYPE html>
<html lang="en">
<head>
<meta charset="utf-8">
<title>TarnWisp – Categories</title>
<link href="https://fonts.googleapis.com/css2?family=Jost:wght@300;400;500&display=swap" rel="stylesheet">
<style>
:root{
  --accent:#f0605a;
  --ink:#222;
  --muted:#555;
  --line:#cfcfcf;
  --star:#f5a623;
  --footer:#262727;
  --footer-base:#212222;
  --footer-text:#d8d8d8;
}
*{margin:0;padding:0;box-sizing:border-box}
html,body{width:861px;height:1200px;overflow:hidden;background:#fff}
body{font-family:'Jost',sans-serif;color:var(--ink);position:relative;font-weight:300}
a{color:inherit;text-decoration:none}
ul{list-style:none}

.site-header{position:absolute;top:19px;left:132px;right:132px;height:20px;display:flex;align-items:center;justify-content:space-between}
.brand{font-size:14px;letter-spacing:2.6px;font-weight:400;color:var(--ink)}
.brand .first{color:var(--accent)}
.main-nav{display:flex;gap:0}
.main-nav a{font-size:8px;font-weight:400;text-transform:uppercase;position:relative;margin-left:33px}
.main-nav a.active::after{content:"";position:absolute;left:50%;top:14px;width:2.5px;height:2.5px;border-radius:50%;background:var(--accent);transform:translateX(-50%)}

.sidebar{position:absolute;left:132px;top:90px;width:110px}
.filter-title{font-size:10px;color:var(--accent);font-weight:400;margin-bottom:11px}
.filter-list li{font-size:8.3px;margin-left:8px;height:22px;line-height:22px}
.filter-list li.current span{border-bottom:1px solid var(--accent);padding-bottom:2px}
.block-brands{position:absolute;top:258px}
.block-size{position:absolute;top:486px}
.sizes{display:grid;grid-template-columns:repeat(4,24px);row-gap:13px;margin-left:8px;font-size:8.5px}
.sizes span.current{text-decoration:underline;text-decoration-color:var(--accent);text-underline-offset:5px;font-weight:400}
.block-color{position:absolute;top:588px}
.swatches{display:grid;grid-template-columns:repeat(4,24px);grid-auto-rows:17.6px;margin-left:7px;margin-top:-2px}

.product-grid{position:absolute;left:257px;top:95px;display:grid;grid-template-columns:repeat(3,148px);column-gap:15px;grid-auto-rows:191px;row-gap:17px}
.card{border:1px solid var(--line);border-radius:13px;overflow:hidden;text-align:center}
.card-image{height:115px}
.rating{color:var(--star);font-size:7px;letter-spacing:0.8px;margin-top:5px;line-height:10px}
.card-kicker{font-size:7.5px;color:var(--muted);margin-top:6px}
.card-title{font-size:9px;font-weight:500;line-height:13.5px;margin-top:2px;letter-spacing:.2px}

.img-tan{background:radial-gradient(ellipse at 50% 60%,#c9a257 0%,#b58d45 35%,#f4f2ee 72%)}
.img-brogue{background:radial-gradient(ellipse at 50% 55%,#7b4a2a 0%,#3b2a22 30%,#f2f2f2 62%)}
.img-slipon{background:radial-gradient(ellipse at 50% 55%,#3a3533 0%,#4a4441 30%,#fafafa 64%)}
.img-oxford{background:radial-gradient(ellipse at 50% 52%,#5a2a22 0%,#6b3a2c 30%,#fbfbfb 64%)}
.img-sneaker{background:radial-gradient(ellipse at 50% 52%,#2e2c25 0%,#3a372e 32%,#ececec 64%)}
.img-derby{background:radial-gradient(ellipse at 55% 52%,#4a3029 0%,#5c3e34 32%,#f6f6f6 66%)}

.site-footer{position:absolute;left:0;top:947px;width:861px;height:212px;background:var(--footer);color:var(--footer-text)}
.footer-logo{position:absolute;left:132px;top:95px;font-size:13px;font-weight:400;color:#fff;letter-spacing:.4px}
.footer-col{position:absolute;top:51px}
.footer-col h3{font-size:9px;font-weight:400;color:#fff;text-transform:uppercase;margin-bottom:10px}
.footer-col li{font-size:8px;height:25px;line-height:10px}
.col-company{left:250px}.col-discover{left:387px}.col-about{left:507px}.col-contact{left:606px}
.contact-item{display:flex;align-items:center;gap:6px}
.contact-item svg{width:7px;height:7px;fill:var(--accent)}
.social{display:flex;align-items:center;gap:12px;margin-left:-1px}
.social .dot{width:8px;height:8px;border-radius:50%;background:#fff}
.footer-base{position:absolute;left:0;top:1159px;width:861px;height:41px;background:var(--footer-base);text-align:center;font-size:7.5px;line-height:41px;color:#777}
.footer-base strong{color:var(--accent);font-weight:500}
</style>
</head>
<body>

<header class="site-header">
  <a class="brand" href="#"><span class="first">TARN</span> WISP</a>
  <nav class="main-nav">
    <a href="#">Home</a><a href="#">Pages</a><a href="#">Blog</a><a class="active" href="#">Categories</a><a href="#">Contact</a>
  </nav>
</header>

<aside class="sidebar">
  <section class="block-categories">
    <h2 class="filter-title">Footwear Categories</h2>
    <ul class="filter-list">
      <li class="current"><span>Boots</span></li><li>Clogs</li><li>Designer Shoes</li><li>Flats</li><li>High Heel Shoes</li><li>Runnin Shoes</li><li>Sandals</li><li>Sneakers</li><li>Slppers</li>
    </ul>
  </section>
  <section class="block-brands">
    <h2 class="filter-title">Brands</h2>
    <ul class="filter-list">
      <li>Corvane</li><li>Stridell</li><li>Hale Tanner</li><li>Fernmoor</li><li>Quillo</li><li>Rendo</li><li>Loftway</li><li>Parkrow</li>
    </ul>
  </section>
  <section class="block-size">
    <h2 class="filter-title">Size</h2>
    <div class="sizes"><span>01</span><span>02</span><span>03</span><span>04</span><span>05</span><span class="current">06</span><span>07</span><span>08</span></div>
  </section>
  <section class="block-color">
    <h2 class="filter-title">Color</h2>
    <div class="swatches">
      <span style="background:#000"></span><span style="background:#808080"></span><span style="background:#ffa500"></span><span style="background:#008000"></span>
      <span style="background:#ff0000"></span><span style="background:#0000ff"></span><span style="background:#f67b3f"></span><span style="background:#adff2f"></span>
      <span style="background:#2f3570"></span><span style="background:#b4363a"></span><span style="background:#8a4e38"></span><span style="background:#eeeef2"></span>
    </div>
  </section>
</aside>

<main class="product-grid">
  <article class="card"><div class="card-image img-tan" role="img" aria-label="Photo of tan leather lace-up hiking boots"></div><div class="rating">★★★★★</div><p class="card-kicker">Lorem Ipsum</p><h3 class="card-title">Premium Quality Boots<br>For Men</h3></article>
  <article class="card"><div class="card-image img-brogue" role="img" aria-label="Photo of brown leather brogue shoes"></div><div class="rating">★★★★★</div><p class="card-kicker">Lorem Ipsum</p><h3 class="card-title">Premium Quality Boots<br>For Men</h3></article>
  <article class="card"><div class="card-image img-slipon" role="img" aria-label="Photo of black slip-on leather shoes"></div><div class="rating">★★★★★</div><p class="card-kicker">Lorem Ipsum</p><h3 class="card-title">Premium Quality Boots<br>For Men</h3></article>
  <article class="card"><div class="card-image img-oxford" role="img" aria-label="Photo of burgundy leather derby shoes"></div><div class="rating">★★★★★</div><p class="card-kicker">Lorem Ipsum</p><h3 class="card-title">Premium Quality Boots<br>For Men</h3></article>
  <article class="card"><div class="card-image img-sneaker" role="img" aria-label="Photo of dark suede sneakers"></div><div class="rating">★★★★★</div><p class="card-kicker">Lorem Ipsum</p><h3 class="card-title">Premium Quality Boots<br>For Men</h3></article>
  <article class="card"><div class="card-image img-derby" role="img" aria-label="Photo of dark brown leather oxford shoes"></div><div class="rating">★★★★★</div><p class="card-kicker">Lorem Ipsum</p><h3 class="card-title">Premium Quality Boots<br>For Men</h3></article>
  <article class="card"><div class="card-image img-tan" role="img" aria-label="Photo of tan leather lace-up hiking boots"></div><div class="rating">★★★★★</div><p class="card-kicker">Lorem Ipsum</p><h3 class="card-title">Premium Quality Boots<br>For Men</h3></article>
  <article class="card"><div class="card-image img-brogue" role="img" aria-label="Photo of brown leather brogue shoes"></div><div class="rating">★★★★★</div><p class="card-kicker">Lorem Ipsum</p><h3 class="card-title">Premium Quality Boots<br>For Men</h3></article>
  <article class="card"><div class="card-image img-slipon" role="img" aria-label="Photo of black slip-on leather shoes"></div><div class="rating">★★★★★</div><p class="card-kicker">Lorem Ipsum</p><h3 class="card-title">Premium Quality Boots<br>For Men</h3></article>
  <article class="card"><div class="card-image img-oxford" role="img" aria-label="Photo of burgundy leather derby shoes"></div><div class="rating">★★★★★</div><p class="card-kicker">Lorem Ipsum</p><h3 class="card-title">Premium Quality Boots<br>For Men</h3></article>
  <article class="card"><div class="card-image img-sneaker" role="img" aria-label="Photo of dark suede sneakers"></div><div class="rating">★★★★★</div><p class="card-kicker">Lorem Ipsum</p><h3 class="card-title">Premium Quality Boots<br>For Men</h3></article>
  <article class="card"><div class="card-image img-derby" role="img" aria-label="Photo of dark brown leather oxford shoes"></div><div class="rating">★★★★★</div><p class="card-kicker">Lorem Ipsum</p><h3 class="card-title">Premium Quality Boots<br>For Men</h3></article>
</main>

<footer class="site-footer">
  <div class="footer-logo">TARNWISP</div>
  <div class="footer-col col-company"><h3>Company</h3><ul><li>Terms of Use</li><li>Privacy Policy</li><li>Editorial Policy</li><li>How We Make Money</li></ul></div>
  <div class="footer-col col-discover"><h3>Discover</h3><ul><li>Terms of Use</li><li>Privacy Policy</li><li>Editorial Policy</li><li>How We Make Money</li></ul></div>
  <div class="footer-col col-about"><h3>About</h3><ul><li>About</li><li>Contact</li><li>Media</li></ul></div>
  <div class="footer-col col-contact"><h3>Contact Info</h3>
    <ul>
      <li class="contact-item"><svg viewBox="0 0 10 10"><path d="M5 0a3.6 3.6 0 0 0-3.6 3.6C1.4 6.3 5 10 5 10s3.6-3.7 3.6-6.4A3.6 3.6 0 0 0 5 0zm0 5a1.4 1.4 0 1 1 0-2.8A1.4 1.4 0 0 1 5 5z"/></svg>48 Orchard Lane, Suite 210</li>
      <li class="contact-item"><svg viewBox="0 0 10 10"><path d="M2.2 0.5 3.8 2.6 2.9 3.8c.6 1.3 1.6 2.3 2.9 2.9l1.2-.9 2.1 1.6-1 1.9C4.2 9.1.5 5.4.4 1.5z"/></svg>01 555 014 732</li>
      <li class="contact-item"><svg viewBox="0 0 10 10"><path d="M0 2h10v6H0z M0 2l5 3.5L10 2" stroke="#262727" stroke-width=".8"/></svg>hello@tarnwisp.com</li>
      <li class="social">Social <span class="dot" aria-label="Social profile"></span><span class="dot" aria-label="Social profile"></span><span class="dot" aria-label="Social profile"></span></li>
    </ul>
  </div>
</footer>
<div class="footer-base">© 2021 <strong>Tarn Wisp</strong>. All right reserved</div>

</body>
</html>
```